Vantor Medica Innovative Business Card

Stunning business card. Background will be black. Letters in gold. Modern yet simple design that is attention grabbing. QR code leading to site. Attractive primarily to males ages 30 to 50 but also to females in same age range looking for beauty and mental health products

Target Market(s)

Males in the 30-50 age demographics

Industry/Entity Type

Pharmaceuticals selling erectile dysfunction and mens health medications

Contact Information for Business Card

www.vantormedica.example; (555) BUY-KELO; info@vantormedica.example

Colors
FFC000
F8CF3A
FAE287
FDF2CF
FEFAEE

Requirements
Must have
• Black business card with gold letters.
Nice to have
• perhaps just the logo or the "R" icon by itself on one side
Should not have
• too much content so it does not look busy

```html
<!DOCTYPE html>
<html lang="en">
<head>
<meta charset="utf-8">
<title>Vantor Medica Business Card</title>
<link rel="stylesheet" href="https://fonts.googleapis.com/css2?family=Poppins:wght@400;700&display=swap">
<style>
  :root {
    --stage-top: #5b6372;
    --stage-bottom: #2b303a;
    --card-black: #0d0d0d;
    --card-edge: #1a1a1a;
    --gold: #d9a81e;
    --rule-grey: #3a3a3a;
  }
  * { box-sizing: border-box; margin: 0; padding: 0; }
  html, body { width: 1200px; height: 900px; overflow: hidden; }
  body {
    background: linear-gradient(160deg, var(--stage-top), var(--stage-bottom));
    font-family: "Poppins", sans-serif;
    position: relative;
  }
  .card {
    position: absolute;
    left: 250px;
    width: 700px;
    height: 400px;
    background: var(--card-black);
    border-radius: 4px;
    box-shadow: 0 14px 30px rgba(0,0,0,.45), 0 0 0 1px var(--card-edge);
    overflow: hidden;
  }
  .card-front { top: 40px; }
  .card-back { top: 460px; }

  .front-brand {
    position: absolute;
    left: 60px;
    top: 120px;
    width: 250px;
    display: flex;
    align-items: center;
    gap: 14px;
  }
  .brand-dot {
    flex: none;
    width: 26px;
    height: 26px;
    border-radius: 50%;
    background: var(--gold);
  }
  .brand-name {
    color: var(--gold);
    font-weight: 700;
    font-size: 34px;
    line-height: 1.05;
    text-transform: uppercase;
    letter-spacing: 1px;
  }
  .divider {
    position: absolute;
    left: 340px;
    top: 90px;
    width: 1px;
    height: 180px;
    background: var(--rule-grey);
  }
  .contact-list {
    position: absolute;
    left: 370px;
    top: 112px;
    list-style: none;
  }
  .contact-item {
    display: flex;
    align-items: center;
    gap: 14px;
    height: 46px;
    color: var(--gold);
    font-size: 17px;
    white-space: nowrap;
  }
  .contact-icon {
    width: 30px;
    height: 30px;
    flex: none;
  }
  .gold-rule {
    position: absolute;
    left: 0;
    right: 40px;
    bottom: 34px;
    height: 4px;
    background: var(--gold);
  }

  .back-brand {
    position: absolute;
    inset: 0;
    display: flex;
    align-items: center;
    justify-content: center;
    gap: 18px;
  }
  .back-brand .brand-dot { width: 34px; height: 34px; }
  .back-brand .brand-name { font-size: 40px; }
</style>
</head>
<body>
  <section class="card card-front" aria-label="Business card front">
    <div class="front-brand">
      <span class="brand-dot"></span>
      <span class="brand-name">Vantor<br>Medica</span>
    </div>
    <div class="divider"></div>
    <ul class="contact-list">
      <li class="contact-item">
        <svg class="contact-icon" viewBox="0 0 30 30" aria-hidden="true">
          <circle cx="15" cy="15" r="13" fill="none" stroke="var(--gold)" stroke-width="1.6"/>
          <path d="M10.5 9.5c1-1 1.8-.9 2.4 0l1 1.6c.4.7.2 1.3-.4 1.8l-.6.5c.6 1.6 1.9 2.9 3.5 3.5l.5-.6c.5-.6 1.1-.8 1.8-.4l1.6 1c.9.6 1 1.4 0 2.4-1.4 1.4-3.6 1-6.2-1.5s-3-4.9-1.6-6.3z" fill="var(--gold)"/>
        </svg>
        <span>(555) BUY-KELO</span>
      </li>
      <li class="contact-item">
        <svg class="contact-icon" viewBox="0 0 30 30" aria-hidden="true">
          <circle cx="15" cy="15" r="13" fill="none" stroke="var(--gold)" stroke-width="1.6"/>
          <rect x="8.5" y="10.5" width="13" height="9" fill="var(--gold)"/>
          <path d="M8.5 10.5l6.5 5 6.5-5" fill="none" stroke="var(--card-black)" stroke-width="1.2"/>
        </svg>
        <span>info@vantormedica.example</span>
      </li>
      <li class="contact-item">
        <svg class="contact-icon" viewBox="0 0 30 30" aria-hidden="true">
          <circle cx="15" cy="15" r="13" fill="none" stroke="var(--gold)" stroke-width="1.6"/>
          <g fill="none" stroke="var(--gold)" stroke-width="1.3">
            <circle cx="15" cy="15" r="7"/>
            <ellipse cx="15" cy="15" rx="3" ry="7"/>
            <path d="M8 15h14M9 11.5h12M9 18.5h12"/>
          </g>
        </svg>
        <span>www.vantormedica.example</span>
      </li>
    </ul>
    <div class="gold-rule"></div>
  </section>

  <section class="card card-back" aria-label="Business card back">
    <div class="back-brand">
      <span class="brand-dot"></span>
      <span class="brand-name">Vantor Medica</span>
    </div>
  </section>
</body>
</html>
```